Pet Resort Website Layout Update for Current Website

Established Dog Daycare, Overnight Care, and Grooming facility in need of a new layout for our website. Our current site is: www.PawHavenLodge.example. We are in the process of re-branding and need a new website to pull our image together.

We are looking to update our look and feel to a more fun and personable layout without looking 'cute'.

The project calls for multiple pages to be created for our final website. However, we are not requiring you to submit all finished pages. To get a good feel for your style that you are presenting please design a home page and two others of your choosing so we may see what you have to offer. If your designs are selected, we will need to work with each other to create the remaining pages needed for the whole website. We are estimating the final product being 10-15 pages.

The new website will use most of our existing content. The home page will need navigation for 'Home', 'About Us', 'Services', 'Get Started', and 'Contact us'.

We like layouts similar to: www.tailwoodpines.example

We like the home page to have a slide show of photos, easy to find phone number, logo, with larger areas to click on for 'Dog Daycare' Overnight Care' Grooming'.

Home page should also have an area spotlighting our new client specials. Testimonials should be found throughout the site, or scrolling in an area on the home page.

Target Market(s)

Dog owners who think of their pets as a member of their family and not 'just a dog'. Families who work long hours or who travel a lot. Women walk through our door more than men. Various ages from 22-65+ . We target a higher income demographic.

Industry/Entity Type

Daycare

Colors
acd036
85cae6
fcfbe6

Requirements
Must have
• Must use the colors of green and blue as provided on the sample file of our business cards. I do not know the actual colors but matching as close as possible is fine with us.

Must be attractive, easy to navigate and find information without feeling overwhelming. Please see an example of at tailwoodpines.example on how we would like to use a photo slide show on the home page.

We will supply photo or stock photography for the final design when the website is put together.

Must be a wordpress design.
Nice to have
• Our final design pages will include:
Home: phone number, logo, slide show, new client offer, facebook tab, client testimonial scrolling or changing area, larger navigation tab for Daycare, Overnight Care and Grooming.

Again the final design chosen will require layouts for more pages. We welcome a design of the front page and two others so we can get a feel for your style before spending the time to create the required 10-15 pages for the final website.
Should not have
• Should not be cluttered with lots of 'noise'. Should not contain clip art. Please make it professional and not 'cute'.

```html
<!DOCTYPE html>
<html lang="en">
<head>
<meta charset="utf-8">
<title>Paw Haven – Pet Resort</title>
<link href="https://fonts.googleapis.com/css2?family=Open+Sans:wght@400;600;700&display=swap" rel="stylesheet">
<style>
:root{
  --lime:#acd036;
  --lime-dark:#8fb21f;
  --lime-pale:#d9ec9c;
  --olive:#33360f;
  --blue:#85cae6;
  --blue-pale:#cfeaf3;
  --blue-dark:#2c8fb5;
  --cream:#fcfbe6;
  --ink:#3d3d3d;
  --white:#ffffff;
}
*{margin:0;padding:0;box-sizing:border-box}
html,body{width:724px;height:1200px;overflow:hidden}
body{font-family:"Open Sans",Arial,sans-serif;color:var(--ink);background:var(--white);position:relative}
.page-top{position:absolute;left:0;top:0;width:724px;height:400px;background:linear-gradient(180deg,var(--lime-pale) 0%,var(--lime) 100%)}
.brand{position:absolute;left:22px;top:14px;display:flex;align-items:center;gap:8px}
.brand-square{width:40px;height:40px;background:var(--olive);border-radius:4px}
.brand-name{font-size:24px;font-weight:700;color:var(--white);letter-spacing:1px;text-transform:uppercase}
.phone{position:absolute;right:22px;top:46px;font-size:21px;font-weight:600;color:var(--olive)}
.social{position:absolute;right:22px;top:14px;display:flex;gap:6px}
.social span{width:22px;height:22px;border-radius:50%;background:var(--olive);display:block}
.main-nav{position:absolute;left:19px;top:87px;width:686px;height:29px;background:var(--olive);display:flex;align-items:center;justify-content:space-around}
.main-nav a{color:var(--white);font-size:12px;font-weight:600;text-decoration:none}
.slider{position:absolute;left:19px;top:116px;width:686px;height:277px;background:linear-gradient(180deg,#cfe3ee 0%,#8fb06a 55%,#4f7a2e 100%)}
.slider-caption{position:absolute;left:0;bottom:0;width:100%;height:26px;background:rgba(30,30,30,.72);color:var(--white);text-align:center;font-size:15px;font-weight:600;line-height:26px}
.slider-arrow{position:absolute;bottom:6px;width:14px;height:14px;border-radius:50%;background:rgba(255,255,255,.8)}
.content{position:absolute;left:0;top:400px;width:724px;height:300px;background:var(--white)}
.services{position:absolute;left:19px;top:22px;width:686px;display:flex;justify-content:space-between}
.service{display:flex;align-items:center;gap:8px}
.service-photo{width:86px;height:86px;border-radius:50%;border:4px solid var(--lime);flex:none}
.service h2{font-size:19px;font-weight:600;color:var(--lime-dark);line-height:1.15;white-space:nowrap}
.service a{font-size:11px;font-weight:700;color:var(--olive);text-decoration:none;white-space:nowrap}
.offer{position:absolute;left:40px;top:132px;width:644px;text-align:center}
.offer h2{font-size:21px;font-weight:600;color:var(--lime-dark);margin-bottom:8px}
.offer p{font-size:10px;line-height:1.55;color:#555}
.btn{display:inline-block;margin-top:14px;background:var(--olive);color:var(--white);font-size:11px;font-weight:700;padding:7px 30px;text-decoration:none}
.testimonials{position:absolute;left:0;top:700px;width:724px;height:156px;background:var(--blue-pale)}
.testimonials h2{position:absolute;left:80px;top:16px;font-size:21px;font-weight:400;color:var(--blue-dark)}
.testimonials blockquote{position:absolute;left:80px;top:56px;width:570px;font-size:10px;line-height:1.5;color:#444}
.testimonials cite{position:absolute;left:80px;top:108px;font-size:11px;font-weight:700;color:var(--blue-dark);font-style:normal}
.t-arrow{position:absolute;top:66px}
.map{position:absolute;left:0;top:900px;width:724px;height:210px;background:linear-gradient(135deg,#ecebe4,#dcdcd2)}
.site-footer{position:absolute;left:0;top:1110px;width:724px;height:90px;background:var(--lime)}
.footer-nav{position:absolute;left:18px;top:10px;font-size:11px;color:var(--olive)}
.footer-nav a{color:var(--olive);text-decoration:none}
.footer-social{position:absolute;left:18px;top:34px;display:flex;gap:6px}
.footer-social span{width:20px;height:20px;border-radius:50%;background:var(--olive);display:block}
.copyright{position:absolute;left:18px;top:66px;font-size:10px;color:var(--olive)}
</style>
</head>
<body>
<header class="page-top">
  <div class="brand"><span class="brand-square"></span><span class="brand-name">Paw Haven</span></div>
  <div class="social"><span></span><span></span></div>
  <div class="phone">Call us: 555 010 2468</div>
</header>
<nav class="main-nav">
  <a href="#">Home</a><a href="#">About us</a><a href="#">Services</a><a href="#">Enrollment</a><a href="#">FAQ</a><a href="#">Pictures</a><a href="#">Location</a><a href="#">Contact</a>
</nav>
<section class="slider" role="img" aria-label="Slideshow photo of two dogs sitting on a green lawn">
  <span class="slider-arrow" style="left:8px"></span>
  <span class="slider-arrow" style="right:8px"></span>
  <div class="slider-caption">Enjoyable pet resort in the Fox Valley</div>
</section>
<main class="content">
  <div class="services">
    <div class="service"><div class="service-photo" role="img" aria-label="Photo of a dog at daycare" style="background:#e8c98a"></div><div><h2>Dog Daycare</h2><a href="#">Learn More ›</a></div></div>
    <div class="service"><div class="service-photo" role="img" aria-label="Photo of a dog resting overnight" style="background:#8a6a4a"></div><div><h2>Overnight Care</h2><a href="#">Learn More ›</a></div></div>
    <div class="service"><div class="service-photo" role="img" aria-label="Photo of a dog being groomed" style="background:#b8c8b0"></div><div><h2>Grooming</h2><a href="#">Learn More ›</a></div></div>
  </div>
  <div class="offer">
    <h2>New Client Offer</h2>
    <p>Lorem gravida nibh vel velit auctor aliquet. Aenean sollicitudin, lorem quis bibendum auctor, nisi elit consequat ipsum, nec sagittis sem nibh id elit. Duis sed odio sit amet nibh vulputate cursus a sit amet mauris. Morbi accumsan ipsum velit. Nam nec tellus a odio tincidunt auctor a ornare odio. Sed non mauris vitae erat consequat auctor eu in elit. Class aptent taciti sociosqu ad litora torquent per.</p>
    <a class="btn" href="#">GET IT</a>
  </div>
</main>
<section class="testimonials">
  <svg class="t-arrow" style="left:18px" width="14" height="24" viewBox="0 0 14 24"><path d="M12 2 2 12l10 10" fill="none" stroke="#fff" stroke-width="3"/></svg>
  <svg class="t-arrow" style="right:18px" width="14" height="24" viewBox="0 0 14 24"><path d="M2 2l10 10L2 22" fill="none" stroke="#fff" stroke-width="3"/></svg>
  <h2>Client Testimonials</h2>
  <blockquote>Every staff member seems to love her as much as we do, and that is very comforting when we travel, and so must board her. We never worry about her when we leave town because we know she will be receiving lots of TLC while we are gone. It is such a pleasure dealing with the friendly and efficient Paw Haven Lodge staff and we w...</blockquote>
  <cite>Client Name, City</cite>
</section>
<div class="map" role="img" aria-label="Street map showing the resort location"></div>
<footer class="site-footer">
  <nav class="footer-nav"><a href="#">Home</a> | <a href="#">About us</a> | <a href="#">Services</a> | <a href="#">Enrollment</a> | <a href="#">FAQ</a> | <a href="#">Pictures</a> | <a href="#">Location</a> | <a href="#">Contact Us</a></nav>
  <div class="footer-social"><span></span><span></span></div>
  <p class="copyright">© 2014 Paw Haven Lodge. All rights reserved.</p>
</footer>
</body>
</html>
```